Our soon to be released website will provide information on any drink and eat deals or other "themed" (recurring) events worth mentioning.
Visitors will be able to find the place they are looking for using tags, location,prices, timings and services.
Examples are: Ladies Night, Brunches, Happy Hour, Iftar, Business Lunch, Hotelier Night, etc.
Launching city = Dubai

Target Market(s)

Visitors of bars, clubs, lounges and restaurants in Dubai

Industry/Entity Type

Events

Contact Information for Business Card

Velvet Hour and Feasts Dubai
Maurits de Klerven
Founder
T +971 (0)50 - 314 2086
E maurits@VvelvetHourandFeastsDubai.example
I www.VelvetHourandFeastsDubai.example
Facebook /velvethourandfeastsdubai
Instagram /velvethour_feasts_dubai/
P.O. Box 347620, Dubai, United Arab Emirates (or) UAE
100% Velvet Hour & Feasts
100% Up-to-date
100% Searchable

Logo Text

Velvet Hour & Feasts (not the word Dubai)

Requirements
Must have
• Business cards should make clear that our company:
• - can attract more visitors for clubs, restaurants, bars etc.
Nice to have
• The website name will be: www.velvethourandfeastsdubai.example
• (and that's also the name of this project).
• We purely decided for this name so everybody knows what we offer (up to date and extensive infromation about recurring drink and eat deals) and it should help us as well in SEO.

```html
<!DOCTYPE html>
<html lang="en">
<head>
<meta charset="utf-8">
<title>Velvet Hour &amp; Feasts – Business Card</title>
<link rel="stylesheet" href="https://fonts.googleapis.com/css2?family=Lato:wght@400;700&display=swap">
<style>
  :root {
    --backdrop: #3a3430;
    --card: #121212;
    --card-edge: #1d1d1d;
    --accent-red: #d42a2a;
    --text-light: #e8e8e8;
    --text-muted: #b5b5b5;
    --mark-grey: #6e6a68;
    --divider: #2c2c2c;
  }
  * { box-sizing: border-box; margin: 0; padding: 0; }
  html, body {
    width: 1200px;
    height: 844px;
    overflow: hidden;
    background: var(--backdrop);
    font-family: "Lato", Arial, sans-serif;
  }
  .stage {
    position: relative;
    width: 1200px;
    height: 844px;
    display: flex;
    align-items: center;
    justify-content: center;
    gap: 60px;
  }
  .card {
    width: 525px;
    height: 300px;
    background: var(--card);
    border: 1px solid var(--card-edge);
    box-shadow: 0 14px 30px rgba(0,0,0,0.45);
    position: relative;
  }
  /* Front side */
  .card--front {
    display: flex;
    align-items: center;
  }
  .brand-block {
    width: 46%;
    display: flex;
    align-items: center;
    justify-content: center;
    gap: 10px;
    padding-left: 18px;
  }
  .brand-square {
    width: 16px;
    height: 16px;
    background: var(--accent-red);
    flex: none;
  }
  .brand-name {
    font-weight: 700;
    font-size: 24px;
    line-height: 1.15;
    color: var(--accent-red);
    letter-spacing: 0.5px;
  }
  .divider {
    width: 1px;
    align-self: stretch;
    margin: 40px 0;
    background: var(--divider);
  }
  .contact-block {
    flex: 1;
    padding-left: 22px;
    color: var(--text-light);
    font-size: 13.5px;
    line-height: 1.45;
  }
  .person-name {
    color: var(--accent-red);
    font-size: 19px;
    font-weight: 400;
    line-height: 1.2;
  }
  .person-role {
    color: var(--text-muted);
    font-size: 12.5px;
    margin-bottom: 16px;
  }
  .address { margin-bottom: 14px; }
  .contact-label { color: var(--accent-red); }
  /* Back side */
  .card--back {
    display: flex;
    align-items: center;
    justify-content: center;
    gap: 12px;
  }
  .card--back .brand-square { background: var(--mark-grey); width: 20px; height: 20px; }
  .card--back .brand-name { color: var(--mark-grey); font-size: 32px; }
</style>
</head>
<body>
  <main class="stage">
    <section class="card card--front" aria-label="Business card front">
      <div class="brand-block">
        <span class="brand-square"></span>
        <span class="brand-name">Velvet Hour &amp;<br>Feasts</span>
      </div>
      <div class="divider"></div>
      <div class="contact-block">
        <p class="person-name">Lucas Brenner</p>
        <p class="person-role">Managing Director</p>
        <p class="address">12345, Address Goes Here<br>Country Name, 123456.</p>
        <p><span class="contact-label">T:</span> 044-000 555 123</p>
        <p><span class="contact-label">E:</span> info@samplemail.example</p>
        <p><span class="contact-label">W:</span> www.samplesite.example</p>
      </div>
    </section>
    <section class="card card--back" aria-label="Business card back">
      <span class="brand-square"></span>
      <span class="brand-name">Velvet Hour &amp; Feasts</span>
    </section>
  </main>
</body>
</html>
```